Black card, Logo on front, in brushed silver, embossed or stamped
details centred on the back of the card written in Serif Old type face
Hotel
Amber Heron Hotel Motel (or smaller logo)
your hosts
Colin and Marisa Doyle
left bottom:
7 Harcourt Street
Wrenfield NSW 2734
right bottom:
P: 02 61739485
M: 0428 315 947
W: www.amberheronhotel.com.au
E: amberheronhotel@mailbox.example
facebook emblem: @AmberHeronHotel
instagram emblem: @amberheronhotel

```html
<!DOCTYPE html>
<html lang="en">
<head>
<meta charset="utf-8">
<title>Amber Heron Hotel – Business Card</title>
<link href="https://fonts.googleapis.com/css2?family=Tinos&display=swap" rel="stylesheet">
<style>
  :root {
    --backdrop: #3b3b3b;
    --card: #050505;
    --silver: #b4b4b4;
    --ink: #f2f2f2;
  }
  * { margin: 0; padding: 0; box-sizing: border-box; }
  html, body {
    width: 1200px; height: 900px; overflow: hidden;
    background: var(--backdrop);
    font-family: "Tinos", "Times New Roman", serif;
  }
  .canvas { position: relative; width: 1200px; height: 900px; }
  .card {
    position: absolute; left: 250px; width: 700px; height: 400px;
    background: var(--card);
    box-shadow: 0 10px 30px rgba(0,0,0,.45);
  }
  .card--front { top: 35px; }
  .card--back { top: 465px; }

  .brand {
    position: absolute; left: 0; right: 0;
    display: flex; flex-direction: column; align-items: center;
    color: var(--silver);
    font-weight: 400;
  }
  .card--front .brand { top: 120px; }
  .card--back .brand { top: 28px; transform: scale(.78); transform-origin: top center; }
  .brand__mark {
    width: 46px; height: 46px; border-radius: 50%;
    background: var(--silver); margin-bottom: 16px;
  }
  .brand__name { font-size: 40px; letter-spacing: 2px; text-transform: uppercase; }
  .brand__place { font-size: 15px; letter-spacing: 7px; text-transform: uppercase; margin-top: 4px; }

  .hosts {
    position: absolute; left: 40px; top: 190px; width: 290px;
    color: var(--ink); text-align: right;
  }
  .hosts__label { font-size: 17px; margin-bottom: 2px; }
  .hosts__names { font-size: 25px; margin-bottom: 26px; }
  .hosts__address { font-size: 19px; line-height: 1.35; }

  .contacts {
    position: absolute; left: 370px; top: 190px;
    list-style: none; color: var(--ink); font-size: 19px;
  }
  .contacts li { display: flex; align-items: center; height: 28px; white-space: nowrap; }
  .contacts svg { width: 16px; height: 16px; margin-right: 12px; flex: none; fill: var(--ink); }
  .social-dot { width: 14px; height: 14px; border-radius: 50%; background: var(--ink); margin: 0 13px 0 1px; flex: none; }
</style>
</head>
<body>
<main class="canvas">
  <section class="card card--front" aria-label="Card front">
    <div class="brand">
      <span class="brand__mark"></span>
      <span class="brand__name">Amber Heron Hotel</span>
      <span class="brand__place">Wrenfield</span>
    </div>
  </section>

  <section class="card card--back" aria-label="Card back">
    <div class="brand">
      <span class="brand__mark"></span>
      <span class="brand__name">Amber Heron Hotel</span>
      <span class="brand__place">Wrenfield</span>
    </div>

    <div class="hosts">
      <p class="hosts__label">your hosts</p>
      <p class="hosts__names">Colin and Marisa Doyle</p>
      <p class="hosts__address">7 Harcourt Street<br>Wrenfield NSW 2734</p>
    </div>

    <ul class="contacts">
      <li><svg viewBox="0 0 16 16" aria-hidden="true"><path d="M3 1l3 3-2 2c1 2 3 4 5 5l2-2 3 3-2 3C7 15 1 9 1 3z"/></svg>02 61739485</li>
      <li><svg viewBox="0 0 16 16" aria-hidden="true"><path d="M4 0h8v16H4zM5.5 2v10h5V2zM7 13h2v2H7z" fill-rule="evenodd"/></svg>0428 315 947</li>
      <li><svg viewBox="0 0 16 16" aria-hidden="true"><circle cx="8" cy="8" r="7" fill="none" stroke="#f2f2f2" stroke-width="1.4"/><path d="M1 8h14M8 1v14" stroke="#f2f2f2" stroke-width="1.2"/><ellipse cx="8" cy="8" rx="3" ry="7" fill="none" stroke="#f2f2f2" stroke-width="1.2"/></svg>www.amberheronhotel.com.au</li>
      <li><svg viewBox="0 0 16 16" aria-hidden="true"><path d="M0 3h16v10H0zM1.5 4.5L8 9l6.5-4.5" fill="none" stroke="#f2f2f2" stroke-width="1.4"/></svg>amberheronhotel@mailbox.example</li>
      <li><span class="social-dot"></span>@AmberHeronHotel</li>
      <li><span class="social-dot"></span>@amberheronhotel</li>
    </ul>
  </section>
</main>
</body>
</html>
```